Design a Website for an IT Support Company

We are an IT support company that provides commercial IT support and services to small and medium sized businesses. We are in need of a website to be developed for our business.
We would like to work with someone who is either familiar with the IT field, or has developed a website for an IT support company in the past.
Some examples of designs/layouts that we like:
https://www.veltragrid.example/
http://www.morvashelp.example/
http://kelbo.example/
http://www.nuvopathsystems.example/
http://www.quordesk.example/
I have attached a word document that gives a menu system/page layout format that we would like for our website as well as branch office phone numbers. Our logo is also attached that you can use for your design purposes. We currently do not have copy produced for all of the pages outlined in the word document, but would get this done during the project with the selected designer.
We would like the website to be SEO friendly & fully responsive. We would prefer a Wordpress format, however, we are open to HTML formats as well.

```html
<!DOCTYPE html>
<html lang="en">
<head>
<meta charset="utf-8">
<title>Corvane IT – Commercial IT Support and Services</title>
<link href="https://fonts.googleapis.com/css2?family=Oswald:wght@300;400;500&family=Open+Sans:wght@400;600;700&display=swap" rel="stylesheet">
<style>
:root{
  --blue:#1a8fd6;
  --blue-deep:#0a4f82;
  --blue-band:#1b76bd;
  --ink:#1f2a36;
  --text:#5d6670;
  --muted:#9aa1a8;
  --light:#f2f4f6;
  --line:#dfe3e7;
  --footer:#a8a8a8;
  --white:#ffffff;
  --head:"Oswald", "Arial Narrow", sans-serif;
  --body:"Open Sans", Arial, sans-serif;
}
*{box-sizing:border-box;margin:0;padding:0}
html,body{width:1200px;height:3056px;overflow:hidden}
body{position:relative;font-family:var(--body);color:var(--text);background:var(--white)}
section,header,footer{position:absolute;left:0;width:1200px}

/* header */
.site-header{top:0;height:92px;background:var(--white)}
.brand{position:absolute;left:252px;top:18px;display:flex;align-items:center;gap:12px}
.brand-dot{width:42px;height:42px;border-radius:50%;background:var(--blue)}
.brand-name{font-family:var(--head);font-weight:500;font-size:32px;color:var(--ink);letter-spacing:.5px}
.main-number{position:absolute;right:254px;top:16px;font-family:var(--head);font-size:15px;color:var(--ink);letter-spacing:.5px;display:flex;align-items:center;gap:6px}
.main-number b{font-weight:500;color:var(--blue-deep)}
.main-nav{position:absolute;right:252px;top:62px;display:flex;gap:22px;font-family:var(--head);font-size:12px;color:var(--blue)}

/* hero */
.hero{top:92px;height:452px}
.hero-photo{position:absolute;inset:0;background:linear-gradient(100deg,#3c6f9c 0%,#2f6b9f 40%,#4d87b9 70%,#2e5f8c 100%)}
.hero-copy{position:absolute;left:257px;top:180px;color:var(--white)}
.hero-kicker{font-family:var(--head);font-size:14px;letter-spacing:.5px}
.hero-title{font-family:var(--head);font-weight:400;font-size:22px;margin-top:6px;letter-spacing:.3px}
.hero-dots{position:absolute;left:582px;top:400px;display:flex;gap:6px}
.hero-dots span{width:10px;height:10px;border-radius:50%;border:2px solid var(--white)}
.hero-dots span.on{background:var(--blue)}

/* services */
.services{top:544px;height:446px}
.section-title{font-family:var(--head);font-weight:400;font-size:24px;text-align:center;color:var(--ink);letter-spacing:.3px}
.section-title em{font-style:normal;color:var(--blue)}
.services .section-title{margin-top:36px}
.service-cards{position:absolute;left:252px;top:82px;display:flex;gap:16px}
.service-card{width:220px;height:310px;border:1px solid var(--line);background:var(--white);position:relative;text-align:center}
.service-photo{height:175px;background:linear-gradient(135deg,#d9dfe5,#9eaab6)}
.service-card:nth-child(2) .service-photo{background:linear-gradient(135deg,#2c4256,#4e7da3)}
.service-card:nth-child(3) .service-photo{background:linear-gradient(135deg,#e6e7e8,#b7a79b)}
.service-icon{position:absolute;left:66px;top:132px;width:88px;height:88px;border-radius:50%;background:#e9ecef;border:4px solid var(--white);display:flex;align-items:center;justify-content:center}
.service-name{margin-top:58px;font-family:var(--head);font-size:12px;color:var(--blue);letter-spacing:.4px}
.service-text{margin:8px 24px 0;font-size:10px;line-height:16px;color:var(--muted)}

/* about */
.about{top:990px;height:381px;background:linear-gradient(180deg,#0c5f97 0%,#0a4c7d 100%);color:var(--white);text-align:center}
.about .section-title{color:var(--white);margin-top:52px}
.about .section-title em{color:#35b3f2}
.about-text{width:620px;margin:26px auto 0;font-size:9.5px;line-height:20px}
.about-text+.about-text{margin-top:12px}
.btn{display:inline-block;margin-top:38px;width:100px;height:27px;line-height:27px;background:var(--blue);font-family:var(--head);font-size:10px;color:var(--white)}

/* overviews */
.overview{top:1371px;height:813px;background:linear-gradient(180deg,#f7f8f9,#eef0f2)}
.divider{width:120px;height:3px;margin:0 auto;background:linear-gradient(90deg,transparent,#9aa3ab 30%,#9aa3ab 70%,transparent);position:relative}
.divider::after{content:"";position:absolute;left:40px;top:-2px;width:40px;height:7px;background:#9aa3ab;border-radius:3px}
.ov-block{position:absolute;left:0;width:1200px}
.ov-block .section-title{margin-top:22px}
.ov-grid{display:grid;grid-template-columns:repeat(5,146px);justify-content:center;row-gap:22px;margin-top:40px}
.ov-item{text-align:center}
.ov-item svg{display:block;margin:0 auto;width:44px;height:40px}
.ov-label{margin-top:8px;font-family:var(--head);font-size:10px;color:var(--ink);letter-spacing:.2px;white-space:nowrap}

/* testimonials */
.testimonials{top:2184px;height:311px;background:linear-gradient(180deg,#1b79c0,#1668aa);color:var(--white);text-align:center}
.testimonials .section-title{color:var(--white);margin-top:48px;font-size:22px}
.avatars{display:flex;justify-content:center;align-items:center;gap:10px;margin-top:18px}
.avatar{width:32px;height:32px;border-radius:50%;background:#8fb6d6;border:2px solid var(--white)}
.avatar.active{width:44px;height:44px;background:#d4dde5}
.quote{width:560px;margin:16px auto 0;font-size:9.5px;line-height:16px}
.quote-dash{width:12px;height:1px;background:var(--white);margin:14px auto 0}
.quote-name{margin-top:8px;font-family:var(--head);font-size:11px;font-weight:500}
.quote-company{font-size:9px;margin-top:2px;color:#d6e7f5}
.quote-mark{position:absolute;left:876px;top:196px}

/* partners */
.partners{top:2495px;height:245px;background:var(--white)}
.partners .section-title{margin-top:56px}
.partner-row{position:absolute;left:250px;top:148px;display:flex;align-items:center;gap:38px}
.partner{background:#c9cdd1}
.partner.wide{width:134px;height:26px}
.partner.round{width:52px;height:52px;border-radius:50%}
.partner.mid{width:84px;height:30px}
.partner.short{width:64px;height:26px}

/* footer */
.site-footer{top:2740px;height:316px;background:var(--footer);color:var(--white)}
.foot-col{position:absolute;top:52px}
.foot-col h3{font-family:var(--head);font-weight:400;font-size:20px;color:#1a6fae;letter-spacing:.3px}
.foot-col ul{list-style:none;margin-top:14px;font-size:9px;line-height:22px}
.col-contact{left:253px}
.col-nav{left:491px}
.col-social{left:729px}
.social{display:flex;gap:5px;margin-top:14px}
.social span{width:18px;height:18px;background:#6f7379}
.badge{margin-top:28px;width:104px;height:40px;background:#2a6ea8;border-radius:3px}
.foot-rule{position:absolute;left:252px;top:265px;width:696px;height:1px;background:#8c8c8c}
.copyright{position:absolute;top:286px;width:1200px;text-align:center;font-size:9px;color:#3d4349}
</style>
</head>
<body>

<svg width="0" height="0" style="position:absolute" aria-hidden="true">
  <defs>
    <symbol id="i-net" viewBox="0 0 44 40"><rect x="15" y="3" width="14" height="9" fill="#2a7fc4"/><rect x="3" y="26" width="12" height="9" fill="#55606b"/><rect x="29" y="26" width="12" height="9" fill="#55606b"/><path d="M22 12v7M9 19h26M9 19v7M35 19v7" stroke="#55606b" stroke-width="2" fill="none"/></symbol>
    <symbol id="i-people" viewBox="0 0 44 40"><circle cx="14" cy="14" r="5" fill="#55606b"/><circle cx="30" cy="14" r="5" fill="#2a7fc4"/><path d="M5 34c0-7 4-11 9-11s9 4 9 11M21 34c0-7 4-11 9-11s9 4 9 11" fill="#55606b"/><circle cx="22" cy="5" r="3" fill="none" stroke="#2a7fc4" stroke-width="1.5"/></symbol>
    <symbol id="i-screen" viewBox="0 0 44 40"><rect x="6" y="5" width="32" height="22" rx="2" fill="none" stroke="#55606b" stroke-width="2"/><rect x="11" y="10" width="22" height="12" fill="#2a7fc4"/><path d="M16 34h12M22 27v7" stroke="#55606b" stroke-width="2"/></symbol>
    <symbol id="i-lock" viewBox="0 0 44 40"><rect x="12" y="17" width="20" height="16" rx="2" fill="#2a7fc4"/><path d="M16 17v-5a6 6 0 0 1 12 0v5" fill="none" stroke="#55606b" stroke-width="2.5"/><circle cx="22" cy="25" r="2.5" fill="#fff"/></symbol>
    <symbol id="i-cloud" viewBox="0 0 44 40"><path d="M12 24a7 7 0 0 1 1-14 9 9 0 0 1 17 2 6 6 0 0 1 2 12z" fill="#55606b"/><path d="M22 26v10M18 32l4 4 4-4" stroke="#2a7fc4" stroke-width="2" fill="none"/></symbol>
    <symbol id="i-server" viewBox="0 0 44 40"><rect x="8" y="6" width="28" height="8" fill="#55606b"/><rect x="8" y="16" width="28" height="8" fill="#2a7fc4"/><rect x="8" y="26" width="28" height="8" fill="#55606b"/><circle cx="31" cy="10" r="1.5" fill="#fff"/><circle cx="31" cy="20" r="1.5" fill="#fff"/><circle cx="31" cy="30" r="1.5" fill="#fff"/></symbol>
    <symbol id="i-wifi" viewBox="0 0 44 40"><rect x="6" y="24" width="32" height="9" rx="2" fill="#2a7fc4"/><path d="M12 24V12M32 24V12" stroke="#55606b" stroke-width="2"/><circle cx="12" cy="29" r="1.5" fill="#fff"/><circle cx="18" cy="29" r="1.5" fill="#fff"/></symbol>
    <symbol id="i-mail" viewBox="0 0 44 40"><rect x="5" y="9" width="30" height="20" fill="none" stroke="#55606b" stroke-width="2"/><path d="M5 9l15 12 15-12" fill="none" stroke="#55606b" stroke-width="2"/><circle cx="35" cy="29" r="6" fill="#2a7fc4"/></symbol>
    <symbol id="i-cable" viewBox="0 0 44 40"><circle cx="14" cy="12" r="6" fill="none" stroke="#55606b" stroke-width="2"/><circle cx="30" cy="26" r="6" fill="none" stroke="#2a7fc4" stroke-width="2"/><path d="M18 16l8 6" stroke="#55606b" stroke-width="2"/></symbol>
    <symbol id="i-phone" viewBox="0 0 44 40"><rect x="8" y="5" width="12" height="30" rx="2" fill="#55606b"/><rect x="22" y="11" width="16" height="24" fill="#2a7fc4"/><path d="M25 16h10M25 21h10M25 26h10" stroke="#fff" stroke-width="2"/></symbol>
    <symbol id="i-star" viewBox="0 0 44 40"><circle cx="22" cy="20" r="14" fill="none" stroke="#2a7fc4" stroke-width="2.5"/><path d="M22 12v16M15 16l14 8M29 16l-14 8" stroke="#55606b" stroke-width="2.5"/></symbol>
    <symbol id="i-building" viewBox="0 0 44 40"><rect x="6" y="12" width="10" height="24" fill="#55606b"/><rect x="17" y="6" width="10" height="30" fill="#2a7fc4"/><rect x="28" y="16" width="10" height="20" fill="#55606b"/></symbol>
    <symbol id="i-headset" viewBox="0 0 44 40"><path d="M10 24v-5a12 12 0 0 1 24 0v5" fill="none" stroke="#55606b" stroke-width="2.5"/><rect x="7" y="22" width="7" height="10" rx="2" fill="#2a7fc4"/><rect x="30" y="22" width="7" height="10" rx="2" fill="#2a7fc4"/></symbol>
  </defs>
</svg>

<header class="site-header">
  <div class="brand"><span class="brand-dot"></span><span class="brand-name">Corvane IT</span></div>
  <div class="main-number">
    <svg width="13" height="13" viewBox="0 0 24 24"><path d="M6.6 10.8a15 15 0 0 0 6.6 6.6l2.2-2.2a1 1 0 0 1 1-.25 11 11 0 0 0 3.6.6 1 1 0 0 1 1 1V20a1 1 0 0 1-1 1A17 17 0 0 1 3 4a1 1 0 0 1 1-1h3.5a1 1 0 0 1 1 1 11 11 0 0 0 .6 3.6 1 1 0 0 1-.25 1z" fill="#1f2a36"/></svg>
    <b>MAIN NUMBER:</b> 972-555-0140
  </div>
  <nav class="main-nav"><span>HOME</span><span>SERVICES</span><span>WHY CORVANE IT</span><span>CONTACT</span></nav>
</header>

<section class="hero">
  <div class="hero-photo" role="img" aria-label="Photo of a technician working at server racks in a data centre, tinted blue"></div>
  <div class="hero-copy">
    <div class="hero-kicker">WE ARE YOUR IT DEPARTMENT</div>
    <h1 class="hero-title">COMMERCIAL IT SUPPORT AND SERVICES</h1>
  </div>
  <div class="hero-dots"><span class="on"></span><span></span><span></span></div>
</section>

<section class="services">
  <h2 class="section-title"><em>CORVANE IT</em> SERVICES</h2>
  <div class="service-cards">
    <article class="service-card">
      <div class="service-photo" role="img" aria-label="Photo of office colleagues working at a laptop"></div>
      <div class="service-icon"><svg width="44" height="40"><use href="#i-net"/></svg></div>
      <h3 class="service-name">DATA SERVICES</h3>
      <p class="service-text">Lorem ipsum dolor sit amet, consectetur adipiscing elit. Nulla nec porttitor justo.</p>
    </article>
    <article class="service-card">
      <div class="service-photo" role="img" aria-label="Photo of hands using a tablet with cloud graphics"></div>
      <div class="service-icon"><svg width="44" height="40"><use href="#i-cloud"/></svg></div>
      <h3 class="service-name">CLOUD SERVICES</h3>
      <p class="service-text">Lorem ipsum dolor sit amet, consectetur adipiscing elit. Nulla nec porttitor justo.</p>
    </article>
    <article class="service-card">
      <div class="service-photo" role="img" aria-label="Photo of support agents wearing headsets"></div>
      <div class="service-icon"><svg width="44" height="40"><use href="#i-headset"/></svg></div>
      <h3 class="service-name">VOICE SERVICES</h3>
      <p class="service-text">Lorem ipsum dolor sit amet, consectetur adipiscing elit. Nulla nec porttitor justo.</p>
    </article>
  </div>
</section>

<section class="about">
  <h2 class="section-title">ABOUT <em>CORVANE IT</em></h2>
  <p class="about-text">Lorem ipsum dolor sit amet, consectetur adipiscing elit. Praesent mollis pellentesque nunc sed ornare. In auctor lectus non ornare imperdiet. Fusce sed fermentum lorem, sit amet ullamcorper sem. Phasellus eu felis, sagittis id egestas id, iaculis sed augue. Suspendisse eget pulvinar lorem, eget efficitur ligula. In lorem risus, viverra vel turpis eget, consectetur accumsan ligula. Nulla id luctus ex. Donec laoreet metus maximus, tempus ipsum eu, ultricies sem. Suspendisse at arcu ligula. Fusce pulvinar, diam a egestas finibus, urna urna mollis tellus, id bibendum tortor leo a mi.</p>
  <p class="about-text">Nullam tempor, erat ut iaculis porta, leo odio ullamcorper libero, vitae mattis nisl tellus sit amet est. Nulla non faucibus urna. Maecenas pretium diam non mi egestas consequat.</p>
  <span class="btn">READ MORE</span>
</section>

<section class="overview">
  <div class="ov-block" style="top:80px">
    <div class="divider"></div>
    <h2 class="section-title"><em>DATA SERVICES</em> OVERVIEW</h2>
    <div class="ov-grid">
      <div class="ov-item"><svg><use href="#i-net"/></svg><div class="ov-label">MANAGED IT SERVICES</div></div>
      <div class="ov-item"><svg><use href="#i-people"/></svg><div class="ov-label">IT SUPPORT &amp; CONSULTIN</div></div>
      <div class="ov-item"><svg><use href="#i-screen"/></svg><div class="ov-label">IT HELPDESK SERVICES</div></div>
      <div class="ov-item"><svg><use href="#i-lock"/></svg><div class="ov-label">NETWORK SECURITY</div></div>
      <div class="ov-item"><svg><use href="#i-cloud"/></svg><div class="ov-label">DATA BACKUP &amp; RECOVERY</div></div>
      <div class="ov-item"><svg><use href="#i-server"/></svg><div class="ov-label">SERVERS &amp; VIRTUALIZATION</div></div>
      <div class="ov-item"><svg><use href="#i-screen"/></svg><div class="ov-label">REMOTE MONITORING SERVICES</div></div>
      <div class="ov-item"><svg><use href="#i-wifi"/></svg><div class="ov-label">WIRELESS NETWORKING</div></div>
      <div class="ov-item"><svg><use href="#i-mail"/></svg><div class="ov-label">EMAIL &amp; SPAM THREAT MANAGEMENT</div></div>
      <div class="ov-item"><svg><use href="#i-cable"/></svg><div class="ov-label">STRUCTURED CABLING</div></div>
    </div>
  </div>

  <div class="ov-block" style="top:388px">
    <div class="divider"></div>
    <h2 class="section-title"><em>CLOUD SERVICES</em> OVERVIEW</h2>
    <div class="ov-grid" style="margin-top:30px">
      <div class="ov-item"><svg><use href="#i-building"/></svg><div class="ov-label">WORKSPACE SUITE MIGRATIONS</div></div>
      <div class="ov-item"><svg><use href="#i-people"/></svg><div class="ov-label">NIMBRA CLOUD MANAGEMENT SERVICES</div></div>
      <div class="ov-item"><svg><use href="#i-cloud"/></svg><div class="ov-label">CLOUD MIGRATION SERVICES</div></div>
      <div class="ov-item"><svg><use href="#i-star"/></svg><div class="ov-label">HOSTED VIRTUAL SERVERS</div></div>
      <div class="ov-item"><svg><use href="#i-screen"/></svg><div class="ov-label">HOSTED TELEPHONE SYSTEMS</div></div>
    </div>
  </div>

  <div class="ov-block" style="top:576px">
    <div class="divider"></div>
    <h2 class="section-title"><em>CLOUD SERVICES</em> OVERVIEW</h2>
    <div class="ov-grid" style="margin-top:36px">
      <div class="ov-item"><svg><use href="#i-star"/></svg><div class="ov-label">ASTREL CONSULTING</div></div>
      <div class="ov-item"><svg><use href="#i-phone"/></svg><div class="ov-label">BUSINESS TELEPHONE</div></div>
      <div class="ov-item"><svg><use href="#i-building"/></svg><div class="ov-label">MULTIPLE OFFICE PHONE</div></div>
      <div class="ov-item"><svg><use href="#i-headset"/></svg><div class="ov-label">GRANVOX TELEPHONE</div></div>
      <div class="ov-item"><svg><use href="#i-phone"/></svg><div class="ov-label">SIP TRUNKS</div></div>
    </div>
  </div>
</section>

<section class="testimonials">
  <h2 class="section-title">TESTIMONIALS</h2>
  <div class="avatars">
    <span class="avatar" role="img" aria-label="Client portrait"></span>
    <span class="avatar active" role="img" aria-label="Client portrait"></span>
    <span class="avatar" role="img" aria-label="Client portrait"></span>
  </div>
  <p class="quote">Lorem ipsum dolor sit amet, consectetur adipiscing elit. Donec maximus sodales tristique. Nulla vitae dui vitae nibh commodo scelerisque sed id lacus. Donec faucibus diam tellus, at maximus nunc dictum at. Phasellus sollicitudin tortor vitae ultrices viverra. Nullam lacus ex, finibus eget interdum nec, elementum ac enim. Nulla facilisi. Nunc dapibus dapibus placerat.</p>
  <div class="quote-dash"></div>
  <div class="quote-name">DANA FERRIS</div>
  <div class="quote-company">Bright Path Training Co.</div>
  <svg class="quote-mark" width="20" height="14" viewBox="0 0 20 14"><path d="M2 12c0-5 2-9 6-10M11 12c0-5 2-9 6-10" stroke="#ffffff" stroke-width="1.6" fill="none" opacity=".8"/></svg>
</section>

<section class="partners">
  <h2 class="section-title"><em>TECHNOLOGY</em> PARTNERS</h2>
  <div class="partner-row">
    <span class="partner wide"></span>
    <span class="partner round"></span>
    <span class="partner mid"></span>
    <span class="partner wide" style="width:104px;height:34px"></span>
    <span class="partner short"></span>
    <span class="partner mid"></span>
  </div>
</section>

<footer class="site-footer">
  <div class="foot-col col-contact">
    <h3>QUICK CONTACT</h3>
    <ul>
      <li>Houston: 832-555-0181</li>
      <li>San Antonio: 210-555-0127</li>
      <li>Austin: 512-555-0163</li>
      <li>Tulsa: 918-555-0109</li>
      <li>Oklahoma City: 405-555-0192</li>
    </ul>
  </div>
  <div class="foot-col col-nav">
    <h3>NAVIGATION</h3>
    <ul>
      <li>Home</li>
      <li>about us</li>
      <li>Why Corvane IT</li>
      <li>Locations</li>
      <li>Terms and Conditions</li>
      <li>Privacy Policy</li>
      <li>Contact us</li>
    </ul>
  </div>
  <div class="foot-col col-social">
    <h3>STAY CONNECTED</h3>
    <div class="social"><span></span><span></span><span></span><span></span><span></span><span></span></div>
    <div class="badge"></div>
  </div>
  <div class="foot-rule"></div>
  <p class="copyright">Copyright © 2017 Corvane IT</p>
</footer>

</body>
</html>
```